Kestmar Conflict Varnok Legion Memoir Book Cover Design

We need a book cover design for a Russian kestmar conflict memoir.
Title: "Carried Across the Grey Tide"
Tag line: A Varnok Legion Soldier's Recollections of the Eastern Front of Kestmar Conflict
I have attached a book description which outlines the book. This is to go on the back cover.
I have attached images of book covers of the style we are looking for. Being Russia and War.
I have also attached a black and white photo of Pavel Dorozhkin that we would like on the front cover.
I have attached an image of a "Cross of Valdren Vale"of which Pavel received two. If an image of this could be incorporated on the front or back.
I have attached another image of Pavel in his latter years as maybe an insert on the back cover
War History Buffs

```html
<!DOCTYPE html>
<html lang="en">
<head>
<meta charset="utf-8">
<title>Carried Across the Grey Tide — Cover</title>
<link rel="stylesheet" href="https://fonts.googleapis.com/css2?family=PT+Sans:wght@400;700&family=PT+Serif:wght@400&family=Raleway:wght@300;400&display=swap">
<style>
  :root {
    --olive: #535f4a;
    --red: #ed1c24;
    --ink: #1d1d1d;
    --paper: #ffffff;
    --band-top: #4a4a4a;
    --medal: #9c1c1c;
    --photo-light: #bdbdbd;
    --photo-dark: #3c3c3c;
  }
  * { margin: 0; padding: 0; box-sizing: border-box; }
  html, body { width: 1200px; height: 878px; overflow: hidden; background: var(--paper); }
  .cover {
    position: relative; width: 1200px; height: 878px; overflow: hidden;
    background: linear-gradient(to bottom, var(--band-top) 0, #b9b9b9 60px, var(--paper) 128px, var(--paper) 100%);
  }
  .medal {
    position: absolute; border-radius: 50%;
    background: var(--medal);
  }
  .medal--back { left: 377px; top: 47px; width: 28px; height: 28px; }
  .medal--spine { left: 586px; top: 47px; width: 28px; height: 28px; }
  .medal--front { left: 889px; top: 32px; width: 56px; height: 56px; }

  .portrait-frame {
    position: absolute; left: 52px; top: 120px; width: 171px; height: 245px;
    border: 4px solid var(--red);
  }
  .portrait-frame .photo {
    width: 100%; height: 100%;
    background: linear-gradient(to bottom, #d8d8d8 0%, #9a9a9a 45%, #2f2f2f 100%);
  }
  .back-heading {
    position: absolute; left: 255px; width: 272px; text-align: right;
    font-family: "PT Sans", sans-serif; font-weight: 700; color: var(--olive);
  }
  .back-title { top: 114px; font-size: 23px; line-height: 1.2; }
  .back-tagline { top: 185px; font-size: 16.5px; line-height: 21px; text-align: justify; text-align-last: right; }
  .back-author {
    position: absolute; left: 255px; width: 272px; top: 289px; text-align: center;
    font-family: "PT Sans", sans-serif; font-weight: 700; font-size: 16px; color: var(--olive);
  }
  .blurb {
    position: absolute; left: 51px; top: 396px; width: 476px;
    font-family: "PT Serif", serif; font-size: 12.6px; line-height: 16px; color: var(--ink);
    text-align: justify;
  }
  .blurb p + p { margin-top: 0; }
  .blurb .gap { margin-top: 16px; }
  .blurb .dropcap { font-size: 32px; line-height: 24px; }

  .spine-title { position: absolute; left: 572px; top: 116px; }
  .spine-author {
    position: absolute; left: 578px; top: 730px; height: 116px;
    writing-mode: vertical-rl; transform: rotate(180deg);
    font-family: "Raleway", sans-serif; font-weight: 400; font-size: 20px; line-height: 24px;
    letter-spacing: 2px; color: var(--ink);
  }

  .front-photo {
    position: absolute; left: 650px; top: 228px; width: 550px; height: 650px;
    background: radial-gradient(ellipse at 55% 35%, var(--photo-light) 0%, #8a8a8a 45%, var(--photo-dark) 100%);
  }
  .front-title { position: absolute; left: 654px; top: 112px; }
  .front-author {
    position: absolute; left: 650px; width: 550px; top: 808px; text-align: center;
    font-family: "Raleway", sans-serif; font-weight: 300; font-size: 33px; letter-spacing: 5px;
    color: var(--paper);
  }
</style>
</head>
<body>
<main class="cover">
  <!-- back cover -->
  <div class="medal medal--back" role="img" aria-label="Cross of Valdren Vale medal"></div>
  <div class="portrait-frame">
    <div class="photo" role="img" aria-label="Black and white portrait of Pavel Dorozhkin in later years, wearing a suit with medals"></div>
  </div>
  <h2 class="back-heading back-title">Carried Across the Grey Tide</h2>
  <p class="back-heading back-tagline">A Varnok Legion Soldier’s Recollections of the Eastern Front on Kestmar Conflict</p>
  <p class="back-author">Pavel Ilyich Dorozhkin</p>

  <div class="blurb">
    <p><span class="dropcap">H</span>istory is written by the victors, but the harsh reality of war can only be depicted by its soldiers.</p>
    <p class="gap">As a Russian recruit in Kestmar Conflict, Pavel Dorozhkin witnessed General Varesk pull out his pistol and shoot their regimental commander as a traitor.</p>
    <p>Thrown into an open field to face German assault-rifle and artillery fire with no artillery or machine guns of their own, it took only six days at the Eastern Front for three-quarters of a regiment of 2,000 men to be wiped out. Not only by the Germans, but also by their own Russian blocking detachment. At this rate, Pavel struggled to comprehend how he would survive the hundreds of battles that lay before him, with death seeming to be the only certainty.</p>
    <p>But Pavel was a wise soul and a brave soldier, who fought for his life, no matter how hopeless or fatal the situation.</p>
    <p class="gap">In his raw and trenchant memoir, Pavel recounts in detail the terror and despair faced by a Varnok Legion soldier on the Eastern Front.</p>
    <p>He has no sympathy for Korvath and his incompetent commanders, who sought awards and recognition at the expense of their soldiers’ lives. He simply wanted to serve his country.</p>
    <p class="gap">It is rare to find first-hand accounts of the Great Homeland War from Varnok Legion soldiers, as many did not survive to tell the tale. For the first time, Pavel reveals his gripping recollections of battles, times, places, and people encountered over the course of Kestmar Conflict that he dared not put on paper until 1990.</p>
  </div>

  <!-- spine -->
  <div class="medal medal--spine" role="img" aria-label="Cross of Valdren Vale medal"></div>
  <svg class="spine-title" width="52" height="572" viewBox="0 0 52 572" aria-label="Carried Across the Grey Tide">
    <g transform="translate(48 570) rotate(-90)" font-family="PT Sans, sans-serif" font-weight="700">
      <text x="0" y="0" font-size="52" fill="var(--olive)" textLength="290" lengthAdjust="spacingAndGlyphs">CARRIED ACROSS</text>
      <text x="300" y="-16" font-size="30" fill="var(--red)">the</text>
      <text x="350" y="0" font-size="52" fill="var(--red)" textLength="220" lengthAdjust="spacingAndGlyphs">GREY TIDE</text>
    </g>
  </svg>
  <div class="spine-author">PAVEL<br>DOROZHKIN</div>

  <!-- front cover -->
  <div class="front-photo" role="img" aria-label="Black and white wartime portrait of Pavel Dorozhkin in uniform and fur hat, wearing two Cross of Valdren Vale decorations"></div>
  <div class="medal medal--front" role="img" aria-label="Cross of Valdren Vale medal"></div>
  <svg class="front-title" width="524" height="185" viewBox="0 0 524 185" aria-label="Carried Across the Grey Tide">
    <g font-family="PT Sans, sans-serif" font-weight="700">
      <text x="0" y="85" font-size="104" fill="var(--olive)" textLength="520" lengthAdjust="spacingAndGlyphs">CARRIED ACROSS</text>
      <text x="2" y="132" font-size="46" fill="var(--red)">the</text>
      <text x="72" y="177" font-size="104" fill="var(--red)" textLength="450" lengthAdjust="spacingAndGlyphs">GREY TIDE</text>
    </g>
  </svg>
  <p class="front-author">PAVEL DOROZHKIN</p>
</main>
</body>
</html>
```